Revamp of existing namecard

Existingly, i've got a namecard that i would like to retain the main design. but there are some changes in my company and i would need to do some amendments to it.

We are a money transfer and money exchange company.
I need 2 different types of name card.
1. For individual name cards
the front to put the following:
Company name and logo
English Name, Chinese Name appointment
Mobile Number, Email and Website.
2 License number under the logo and name

the back of the name card to put
8 address: 7 Singapore and 1 Hong Kong branch addresses
8 Mobile Number of the corresponding addresses.

We would like to retain the name card front design
the name card back design can change but color to retain.

2nd name card is generic name card
Front:
Company name and logo
Branch Mobile Number, Branch Address, Email and Website.

Industry/Entity Type

remittance and money exchange

Contact Information for Business Card

I need 2 different types of name card. 1. For individual name cards the front to put the following: Company name and logo English Name, Chinese Name appointment Mobile Number, Email and Website. 2 License number under the logo and name the back of the name card to put 8 address: 7 Singapore and 1 Hong Kong branch addresses 8 Mobile Number of the corresponding addresses. We would like to retain the name card front design the name card back design can change but color to retain. 2nd name card is generic name card Front: the front to put the following: Company name and logo Branch Mobile Number, Branch Address, Email and Website. 2 License number under the logo and name

Requirements
Must have
• I need 2 different types of name card. 1. For individual name cards the front to put the following: Company name and logo English Name, Chinese Name appointment Mobile Number, Email and Website. 2 License number under the logo and name the back of the name card to put 8 address: 7 Singapore and 1 Hong Kong branch addresses 8 Mobile Number of the corresponding addresses. We would like to retain the name card front design the name card back design can change but color to retain. 2nd name card is generic name card Front: the front to put the following: Company name and logo Branch Mobile Number, Branch Address, Email and Website. 2 License number under the logo and name
Nice to have
• use back color code

```html
<!DOCTYPE html>
<html lang="en">
<head>
<meta charset="utf-8">
<title>Norvale business cards</title>
<link rel="stylesheet" href="https://fonts.googleapis.com/css2?family=Montserrat:wght@400;500;600;700&family=Open+Sans:wght@400&family=Noto+Sans+TC:wght@700&display=swap">
<style>
  :root {
    --page: #e6e6e6;
    --paper: #ffffff;
    --ink: #2d3a48;
    --ink-soft: #3c4550;
    --teal: #7ec8d9;
    --map: #eef0f2;
    --night: #000000;
    --night-shape: #1f1f1f;
    --white: #ffffff;
  }
  * { margin: 0; padding: 0; box-sizing: border-box; }
  html, body { width: 1200px; height: 1200px; overflow: hidden; }
  body { background: var(--page); position: relative; font-family: "Montserrat", sans-serif; }

  .card { position: absolute; width: 576px; height: 336px; overflow: hidden; }
  .card--front { background: var(--paper); top: 209px; }
  .card--back { background: var(--night); top: 653px; }
  .card--left { left: 19px; }
  .card--right { left: 605px; }

  .world-map {
    position: absolute; left: 10px; top: 40px; width: 530px; height: 268px;
    background: radial-gradient(ellipse at 50% 45%, var(--map) 0%, var(--map) 55%, rgba(238,240,242,0) 75%);
  }

  .brand { position: absolute; display: flex; align-items: center; gap: 10px; }
  .brand__mark { width: 30px; height: 30px; background: var(--teal); border-radius: 50%; }
  .brand__name { font-weight: 600; letter-spacing: 0.5px; line-height: 1; }
  .brand--front { left: 257px; top: 38px; }
  .brand--front .brand__name { font-size: 34px; color: var(--ink); }
  .brand--back { left: 0; right: 0; top: 148px; justify-content: center; }
  .brand--back .brand__mark { width: 38px; height: 38px; }
  .brand--back .brand__name { font-size: 42px; color: var(--white); }

  .person { position: absolute; left: 32px; top: 134px; }
  .person__name { font-size: 22px; font-weight: 700; color: var(--ink); line-height: 26px; letter-spacing: 0.3px; }
  .person__name-zh { font-family: "Noto Sans TC", sans-serif; font-size: 20px; font-weight: 700; color: var(--ink); line-height: 24px; }
  .person__title { font-size: 14px; font-weight: 400; color: var(--teal); line-height: 22px; }

  .address { position: absolute; font-size: 12.5px; line-height: 20px; color: var(--ink-soft); }
  .address--front-a { left: 321px; top: 139px; font-family: "Montserrat", sans-serif; }
  .address--front-b { left: 319px; top: 139px; font-family: "Open Sans", sans-serif; font-size: 13px; }
  .address--back { left: 21px; color: var(--white); font-family: "Open Sans", sans-serif; font-size: 13px; }
  .address--back-a { top: 249px; font-family: "Montserrat", sans-serif; font-size: 12.5px; }
  .address--back-b { top: 256px; }

  .contacts { position: absolute; list-style: none; font-size: 13px; color: var(--ink-soft); letter-spacing: 0.6px; }
  .contacts li { display: flex; align-items: center; gap: 6px; height: 22px; }
  .contacts svg { width: 12px; height: 12px; flex: none; }
  .contacts--front-a { left: 321px; top: 214px; }
  .contacts--front-b { left: 319px; top: 236px; }
  .contacts--back { color: var(--white); }
  .contacts--back-a { left: 391px; top: 265px; }
  .contacts--back-b { left: 389px; top: 290px; font-size: 12px; letter-spacing: 1.5px; }

  .back-shape {
    position: absolute; left: 100px; top: 10px; width: 376px; height: 376px;
    border-radius: 50%; background: var(--night-shape);
  }
</style>
</head>
<body>

  <!-- Front, two phone lines -->
  <section class="card card--front card--left">
    <div class="world-map" role="img" aria-label="Dotted world map in pale grey"></div>
    <div class="brand brand--front"><span class="brand__mark"></span><span class="brand__name">NORVALE</span></div>
    <div class="person">
      <p class="person__name">Marcus Leung</p>
      <p class="person__name-zh">梁志明</p>
      <p class="person__title">Director of Business Development</p>
    </div>
    <address class="address address--front-a" style="font-style:normal">
      Unit 1805, 18th Floor<br>Harbourview Tower<br>12 Kingsley Road, Wan Chai
    </address>
    <ul class="contacts contacts--front-a">
      <li><svg viewBox="0 0 12 12"><rect x="3" y="0.5" width="6" height="11" rx="1.2" fill="none" stroke="var(--teal)" stroke-width="1.2"/><circle cx="6" cy="9.6" r="0.7" fill="var(--teal)"/></svg>+852 5123 4401</li>
      <li><svg viewBox="0 0 12 12"><path d="M2.5 1 L4.5 1 L5.5 3.5 L4 4.7 C4.8 6.5 5.6 7.3 7.3 8 L8.5 6.5 L11 7.5 L11 9.5 C11 10.5 10 11 9 11 C4.5 10.5 1.5 7.5 1 3 C1 2 1.5 1 2.5 1 Z" fill="var(--teal)"/></svg>+852 5234 8812</li>
      <li><svg viewBox="0 0 12 12"><rect x="0.5" y="2.5" width="11" height="7.5" fill="var(--teal)"/><path d="M0.5 2.5 L6 7 L11.5 2.5" fill="none" stroke="var(--paper)" stroke-width="1"/></svg>marcus@norvale.com.hk</li>
      <li><svg viewBox="0 0 12 12"><circle cx="6" cy="6" r="5" fill="none" stroke="var(--teal)" stroke-width="1.1"/><ellipse cx="6" cy="6" rx="2.2" ry="5" fill="none" stroke="var(--teal)" stroke-width="1"/><path d="M1 6 H11" stroke="var(--teal)" stroke-width="1"/></svg>www.norvale.com.hk</li>
    </ul>
  </section>

  <!-- Front, branch -->
  <section class="card card--front card--right">
    <div class="world-map" role="img" aria-label="Dotted world map in pale grey"></div>
    <div class="brand brand--front" style="left:255px"><span class="brand__mark"></span><span class="brand__name">NORVALE</span></div>
    <div class="person">
      <p class="person__name">Marcus Leung</p>
      <p class="person__name-zh">梁志明</p>
      <p class="person__title">Director of Business Development</p>
    </div>
    <address class="address address--front-b" style="font-style:normal">
      12/F Carlton Point,<br>5-7 Carlton Road,<br>Mong Kok
    </address>
    <ul class="contacts contacts--front-b">
      <li><svg viewBox="0 0 12 12"><rect x="3" y="0.5" width="6" height="11" rx="1.2" fill="none" stroke="var(--teal)" stroke-width="1.2"/><circle cx="6" cy="9.6" r="0.7" fill="var(--teal)"/></svg>+852 52348812</li>
      <li><svg viewBox="0 0 12 12"><rect x="0.5" y="2.5" width="11" height="7.5" fill="var(--teal)"/><path d="M0.5 2.5 L6 7 L11.5 2.5" fill="none" stroke="var(--paper)" stroke-width="1"/></svg>marcus@norvale.com.hk</li>
      <li><svg viewBox="0 0 12 12"><circle cx="6" cy="6" r="5" fill="none" stroke="var(--teal)" stroke-width="1.1"/><ellipse cx="6" cy="6" rx="2.2" ry="5" fill="none" stroke="var(--teal)" stroke-width="1"/><path d="M1 6 H11" stroke="var(--teal)" stroke-width="1"/></svg>www.norvale.com.hk</li>
    </ul>
  </section>

  <!-- Back, two phone lines -->
  <section class="card card--back card--left">
    <div class="back-shape"></div>
    <div class="brand brand--back"><span class="brand__mark"></span><span class="brand__name">NORVALE</span></div>
    <address class="address address--back address--back-a" style="font-style:normal">
      Unit 1805, 18th Floor<br>Harbourview Tower<br>12 Kingsley Road, Wan Chai
    </address>
    <ul class="contacts contacts--back contacts--back-a">
      <li><svg viewBox="0 0 12 12"><rect x="3" y="0.5" width="6" height="11" rx="1.2" fill="none" stroke="var(--teal)" stroke-width="1.2"/><circle cx="6" cy="9.6" r="0.7" fill="var(--teal)"/></svg>+852 5123 4401</li>
      <li><svg viewBox="0 0 12 12"><path d="M2.5 1 L4.5 1 L5.5 3.5 L4 4.7 C4.8 6.5 5.6 7.3 7.3 8 L8.5 6.5 L11 7.5 L11 9.5 C11 10.5 10 11 9 11 C4.5 10.5 1.5 7.5 1 3 C1 2 1.5 1 2.5 1 Z" fill="var(--teal)"/></svg>+852 5234 8812</li>
    </ul>
  </section>

  <!-- Back, branch -->
  <section class="card card--back card--right">
    <div class="back-shape"></div>
    <div class="brand brand--back"><span class="brand__mark"></span><span class="brand__name">NORVALE</span></div>
    <address class="address address--back address--back-b" style="font-style:normal">
      12/F Carlton Point,<br>5-7 Carlton Road,<br>Mong Kok
    </address>
    <ul class="contacts contacts--back contacts--back-b">
      <li><svg viewBox="0 0 12 12"><rect x="3" y="0.5" width="6" height="11" rx="1.2" fill="none" stroke="var(--teal)" stroke-width="1.2"/><circle cx="6" cy="9.6" r="0.7" fill="var(--teal)"/></svg>+852 52348812</li>
    </ul>
  </section>

</body>
</html>
```